Email Banner (LumenBriefs)

We require an email banner for our email promotions sent to prospect clients. The banner needs to contain the wording LumenBriefs and use the same colour scheme as the logos attached.

This is for B2B professional's so needs to look like a place you would come to read technology articles.

```html
<!DOCTYPE html>
<html lang="en">
<head>
<meta charset="utf-8">
<title>LumenBriefs Email Banner</title>
<link rel="stylesheet" href="https://fonts.googleapis.com/css2?family=Montserrat:ital,wght@0,400;0,500;0,600;1,300;1,400;1,700&display=swap">
<style>
  :root {
    --navy: #03182b;
    --teal: #1a9bb8;
    --blue: #1a8fd0;
    --green: #7cc242;
    --green-deep: #3aa873;
    --ink: #0b1a2c;
    --grey-text: #6e7479;
    --page: #e9ebed;
    --white: #ffffff;
  }
  * { margin: 0; padding: 0; box-sizing: border-box; }
  html, body { width: 1200px; height: 661px; overflow: hidden; }
  body {
    background: var(--page);
    font-family: "Montserrat", sans-serif;
    display: flex; align-items: center; justify-content: center;
  }
  .banner {
    position: relative;
    width: 1200px; height: 428px;
    overflow: hidden;
    background: linear-gradient(90deg, #e6e8ea 0%, #fbfbfb 45%, #eceef0 100%);
  }
  .banner-art { position: absolute; inset: 0; }
  .brand {
    position: absolute; right: 41px; top: 44px;
    display: flex; align-items: center; gap: 8px;
  }
  .brand-mark { width: 16px; height: 16px; background: var(--teal); }
  .brand-name { font-size: 28px; font-weight: 600; color: var(--ink); letter-spacing: -0.3px; }
  .headline {
    position: absolute; right: 41px; top: 140px;
    font-size: 34px; font-style: italic; font-weight: 300; color: var(--ink);
  }
  .headline strong { font-weight: 700; }
  .intro {
    position: absolute; right: 41px; top: 186px; width: 520px;
    text-align: right; font-size: 14.2px; line-height: 18.6px;
    font-style: italic; font-weight: 300; color: var(--grey-text);
  }
  .web-address {
    position: absolute; left: 634px; top: 302px;
    font-size: 17px; font-style: italic; font-weight: 500;
    letter-spacing: 6.4px; color: var(--ink);
  }
  .btn {
    position: absolute; top: 302px; height: 28px; width: 97px;
    border-radius: 14px; font-size: 12px; font-weight: 600;
    display: flex; align-items: center; justify-content: center;
  }
  .btn-skip { left: 951px; background: var(--navy); color: var(--white); }
  .btn-more { left: 1062px; border: 1.5px solid var(--navy); color: var(--navy); }
  .social { position: absolute; left: 362px; top: 368px; display: flex; gap: 27px; }
  .social-dot { width: 33px; height: 33px; border-radius: 50%; background: var(--green); }
  .contact {
    position: absolute; top: 375px; display: flex; align-items: center; gap: 10px;
    font-size: 17px; color: var(--white); font-weight: 400;
  }
  .contact-phone { left: 738px; }
  .contact-mail { left: 950px; }
  .contact svg { display: block; }
</style>
</head>
<body>
<div class="banner">
  <svg class="banner-art" width="1200" height="428" viewBox="0 0 1200 428">
    <defs>
      <linearGradient id="ring-grad" x1="0" y1="0" x2="1" y2="1">
        <stop offset="0" stop-color="#1a8fd0"/><stop offset="1" stop-color="#7cc242"/>
      </linearGradient>
      <linearGradient id="blob-grad" x1="0" y1="0" x2="1" y2="1">
        <stop offset="0" stop-color="#2f9e7a"/><stop offset="0.6" stop-color="#1fa0b0"/><stop offset="1" stop-color="#1a9bb8"/>
      </linearGradient>
      <linearGradient id="rim-grad" x1="0" y1="0" x2="1" y2="1">
        <stop offset="0" stop-color="#3aa873"/><stop offset="1" stop-color="#7cc242"/>
      </linearGradient>
      <linearGradient id="band-grad" x1="0" y1="0" x2="1" y2="0">
        <stop offset="0" stop-color="#1a9bb8"/><stop offset="0.55" stop-color="#3fad86"/><stop offset="1" stop-color="#7cc242"/>
      </linearGradient>
      <linearGradient id="photo-grey" x1="0" y1="0" x2="1" y2="1">
        <stop offset="0" stop-color="#d9dbdd"/><stop offset="1" stop-color="#7d8185"/>
      </linearGradient>
      <linearGradient id="photo-office" x1="0" y1="0" x2="1" y2="1">
        <stop offset="0" stop-color="#eef1f3"/><stop offset="0.6" stop-color="#8a97a8"/><stop offset="1" stop-color="#2d3b55"/>
      </linearGradient>
    </defs>

    <path d="M0,0 L140,0 C60,40 0,120 0,200 Z" fill="#e3e5e7"/>
    <circle cx="217" cy="210" r="172" fill="url(#photo-grey)" role="img" aria-label="Photo: hand pointing at a chart on a laptop screen, in greyscale"/>

    <path d="M270,46 C215,80 180,150 185,220 C190,270 215,310 250,339 L470,339 L470,291 L300,291 Z" fill="url(#blob-grad)"/>
    <circle cx="396" cy="220" r="146" fill="url(#rim-grad)"/>
    <path d="M520,195 C524,222 540,232 562,232 L590,232 C598,232 601,240 598,250 L585,291 L440,291 L440,200 Z" fill="url(#rim-grad)"/>
    <rect x="440" y="291" width="760" height="48" fill="url(#band-grad)"/>
    <rect x="250" y="291" width="200" height="48" fill="#1f9db0"/>

    <path d="M138,428 C200,385 270,350 340,339 L1200,339 L1200,428 Z" fill="var(--navy)"/>

    <circle cx="387" cy="216" r="128" fill="none" stroke="var(--blue)" stroke-width="11"/>
    <circle cx="387" cy="216" r="117" fill="url(#photo-office)" role="img" aria-label="Photo: man in a checked shirt working on a laptop at a desk"/>

    <circle cx="145" cy="57" r="16" fill="none" stroke="url(#ring-grad)" stroke-width="3"/>
    <circle cx="569" cy="86" r="26" fill="none" stroke="url(#ring-grad)" stroke-width="4"/>
    <circle cx="89" cy="333" r="45" fill="none" stroke="url(#ring-grad)" stroke-width="6"/>
  </svg>

  <div class="brand">
    <span class="brand-mark"></span>
    <span class="brand-name">LumenBriefs.io</span>
  </div>

  <h1 class="headline"><strong>Our</strong> Business</h1>
  <p class="intro">Lorem ipsum dolor sit amet, copiosae vituperata vix an. Postea bono-<br>rum placerat cu his, nam quas recteque in,<br>ea sea iuvaret mandamus. Lorem ipsum dolor sit amet, copiosae<br>vituperata vix an. Postea bonorum</p>

  <div class="web-address">www.lumenbriefs.io</div>
  <div class="btn btn-skip">SKIP</div>
  <div class="btn btn-more">MORE</div>

  <div class="social" aria-label="Social media links">
    <span class="social-dot"></span>
    <span class="social-dot"></span>
    <span class="social-dot"></span>
    <span class="social-dot"></span>
    <span class="social-dot"></span>
  </div>

  <div class="contact contact-phone">
    <svg width="18" height="14" viewBox="0 0 18 14"><path d="M1,5 C1,1 17,1 17,5 L13,6 L12,3.5 L6,3.5 L5,6 Z" fill="var(--green)"/><rect x="3" y="7" width="12" height="6" rx="1" fill="var(--green)"/><circle cx="9" cy="10" r="1.8" fill="var(--navy)"/></svg>
    <span>+000 123 456 789</span>
  </div>
  <div class="contact contact-mail">
    <svg width="20" height="14" viewBox="0 0 20 14"><rect x="1" y="1" width="18" height="12" fill="none" stroke="var(--green)" stroke-width="1.6"/><path d="M1,1 L10,8 L19,1" fill="none" stroke="var(--green)" stroke-width="1.6"/></svg>
    <span>info@lumenbriefs.io</span>
  </div>
</div>
</body>
</html>
```